Business cards Dorn Kelterhof GmbH & Co.KG

We need a uniform business card design template for our employees.
A template should be created to have the same design for all business cards.

Contact Information for Business Card

Firma und Firmierung, Name, Funktion in Unternehmen, Anschrift, Tel. Handynummer, Emailadresse, Internetseite

Colors

Designer to choose colors to be used in the design.

Requirements
Must have
• Our company logo must be on it

```html
<!DOCTYPE html>
<html lang="de">
<head>
<meta charset="utf-8">
<title>Visitenkarten – Dorn Kelterhof GmbH &amp; Co.KG</title>
<link rel="stylesheet" href="https://fonts.googleapis.com/css2?family=Montserrat:wght@500;800&family=Open+Sans:wght@400;600&display=swap">
<style>
  :root {
    --stage: #2e2a28;
    --card-light: #713c33;
    --card-dark: #552c27;
    --pink: #f07f8f;
    --lilac: #c9a0d6;
    --white: #ffffff;
  }
  * { box-sizing: border-box; margin: 0; padding: 0; }
  html, body { width: 1200px; height: 1200px; overflow: hidden; }
  body {
    background: var(--stage);
    display: flex;
    flex-direction: column;
    align-items: center;
    justify-content: center;
    gap: 40px;
    font-family: "Open Sans", sans-serif;
  }
  .card {
    position: relative;
    width: 960px;
    height: 549px;
    background: radial-gradient(ellipse at 50% 45%, var(--card-light) 0%, var(--card-dark) 75%);
    box-shadow: 0 10px 30px rgba(0,0,0,0.45);
    color: var(--white);
  }
  .brand-name {
    font-family: "Montserrat", sans-serif;
    font-weight: 500;
    color: var(--lilac);
    letter-spacing: 1px;
    white-space: nowrap;
  }

  /* Front */
  .card-front .brand-name {
    position: absolute;
    top: 170px;
    left: 0; right: 0;
    text-align: center;
    font-size: 66px;
  }
  .card-front .accent-wedges {
    position: absolute;
    left: 0; top: 370px;
    width: 960px; height: 60px;
  }
  .card-front .website {
    position: absolute;
    top: 378px;
    left: 0; right: 0;
    text-align: center;
    font-size: 34px;
    font-weight: 600;
    letter-spacing: 0.5px;
  }

  /* Back */
  .card-back .brand-name {
    position: absolute;
    top: 120px;
    left: 110px;
    font-size: 48px;
  }
  .card-back .person {
    position: absolute;
    left: 110px;
    top: 360px;
  }
  .person-name {
    font-family: "Montserrat", sans-serif;
    font-weight: 800;
    font-size: 44px;
    letter-spacing: 1px;
    line-height: 1.1;
  }
  .person-role {
    font-family: "Montserrat", sans-serif;
    font-weight: 500;
    font-size: 26px;
    color: var(--pink);
  }
  .divider {
    position: absolute;
    left: 560px;
    top: 180px;
    width: 4px;
    height: 250px;
    background: var(--lilac);
  }
  .contact-list {
    position: absolute;
    left: 600px;
    top: 190px;
    list-style: none;
  }
  .contact-list li {
    display: flex;
    align-items: center;
    gap: 16px;
    height: 56px;
    font-size: 26px;
  }
  .contact-list svg {
    width: 26px; height: 26px;
    flex: none;
  }
</style>
</head>
<body>

  <section class="card card-front">
    <div class="brand-name">Dorn Kelterhof</div>
    <svg class="accent-wedges" viewBox="0 0 960 60" aria-hidden="true">
      <polygon points="40,56 250,14 250,32" fill="var(--pink)"/>
      <polygon points="920,4 710,28 710,46" fill="var(--pink)"/>
    </svg>
    <div class="website">WWW.WEBSITEHERE.COM</div>
  </section>

  <section class="card card-back">
    <div class="brand-name">Dorn Kelterhof</div>
    <div class="person">
      <div class="person-name">LENA HARTMANN</div>
      <div class="person-role">Manager</div>
    </div>
    <div class="divider"></div>
    <ul class="contact-list">
      <li>
        <svg viewBox="0 0 24 24" aria-hidden="true"><rect x="6" y="2" width="12" height="20" rx="2" fill="none" stroke="var(--pink)" stroke-width="2"/><circle cx="12" cy="18.5" r="1.2" fill="var(--pink)"/></svg>
        <span>+0000-000-0000</span>
      </li>
      <li>
        <svg viewBox="0 0 24 24" aria-hidden="true"><path d="M6.6 10.8a15 15 0 0 0 6.6 6.6l2.2-2.2a1 1 0 0 1 1-.25 11.4 11.4 0 0 0 3.6.57 1 1 0 0 1 1 1V20a1 1 0 0 1-1 1A17 17 0 0 1 3 4a1 1 0 0 1 1-1h3.5a1 1 0 0 1 1 1c0 1.25.2 2.45.57 3.6a1 1 0 0 1-.25 1z" fill="var(--pink)"/></svg>
        <span>+0000-000-0000</span>
      </li>
      <li>
        <svg viewBox="0 0 24 24" aria-hidden="true"><rect x="2" y="5" width="20" height="14" rx="1" fill="var(--pink)"/><path d="M2.5 6 12 13l9.5-7" fill="none" stroke="var(--card-dark)" stroke-width="1.6"/></svg>
        <span>email@addresshere.com</span>
      </li>
      <li>
        <svg viewBox="0 0 24 24" aria-hidden="true"><g fill="none" stroke="var(--pink)" stroke-width="1.6"><circle cx="12" cy="12" r="9.5"/><ellipse cx="12" cy="12" rx="4" ry="9.5"/><path d="M2.5 12h19M4 7h16M4 17h16"/></g></svg>
        <span>www.websitehere.com</span>
      </li>
    </ul>
  </section>

</body>
</html>
```